Letterhead Design

We need a new Letterhead design for a 30 year old Electrical Company. We service domestic and commercial places. We have a logo recently made so to incorporate that. Using same colours or interested to see others added.
Would like to see a couple of options with all the info in letterhead, then another with info in a footnote down the bottom.

info needed to be added:

-Lic. No 48162
8/22-24 Larkin Rd, Tolvern 2087
W - brightcoilpower.com.au
T - (02) 9471 3825
M - 0427 593 168
E - info@brightcoilpower.com.au
ABN: 42 597 214 630

Electrical

```html
<!DOCTYPE html>
<html lang="en">
<head>
<meta charset="utf-8">
<title>Brightcoil Power Electrical – Letterhead</title>
<link rel="stylesheet" href="https://fonts.googleapis.com/css2?family=Lato:wght@400;700&family=Dancing+Script:wght@500&display=swap">
<style>
  :root {
    --backdrop: #e9e9e9;
    --paper: #ffffff;
    --ink: #2b2b2b;
    --ink-soft: #444444;
    --brand-dark: #0f2826;
    --brand-orange: #f29a1f;
    --signature: #27307a;
  }
  * { box-sizing: border-box; margin: 0; padding: 0; }
  html, body {
    width: 1200px; height: 795px; overflow: hidden;
    background: var(--backdrop);
    font-family: "Lato", Arial, sans-serif;
    color: var(--ink);
  }
  .letterhead {
    position: absolute; left: 338px; top: 27px;
    width: 523px; height: 740px;
    background: var(--paper);
    box-shadow: 0 2px 10px rgba(0,0,0,.12);
    overflow: hidden;
  }
  .brand {
    position: absolute; left: 40px; top: 118px;
    display: flex; align-items: center; gap: 6px;
  }
  .brand-mark { width: 9px; height: 9px; background: var(--brand-orange); }
  .brand-name {
    font-size: 17px; font-weight: 700; color: var(--brand-dark);
    letter-spacing: .2px;
  }
  .company-details {
    position: absolute; right: 36px; top: 30px;
    text-align: right; font-size: 6.4px; line-height: 1.45;
    color: var(--ink-soft);
  }
  .company-details .company-title { font-weight: 700; color: var(--ink); }
  .company-details .label { color: var(--brand-orange); }
  .detail-row { display: flex; justify-content: flex-end; align-items: center; gap: 3px; }
  .detail-icon { width: 6px; height: 6px; background: var(--brand-orange); border-radius: 1px; display: inline-block; }
  .letter {
    position: absolute; left: 40px; top: 170px; width: 440px;
    font-size: 7.2px; line-height: 1.5; color: var(--ink-soft);
  }
  .salutation { font-size: 8px; font-weight: 700; color: var(--ink); margin-bottom: 10px; }
  .letter p { margin-bottom: 10px; }
  .sign-off { margin-top: 14px; font-size: 7.6px; color: var(--ink); }
  .signature {
    font-family: "Dancing Script", cursive;
    font-size: 22px; color: var(--signature); line-height: 1.1; margin: 2px 0 0 8px;
  }
  .signer { font-size: 7.6px; color: var(--ink); line-height: 1.4; }
  .footer-wave { position: absolute; left: 0; bottom: 0; width: 523px; height: 740px; }
  .footer-web {
    position: absolute; right: 28px; bottom: 22px;
    font-size: 10px; letter-spacing: .4px; color: var(--brand-orange);
  }
</style>
</head>
<body>
  <main class="letterhead">
    <header>
      <div class="brand">
        <span class="brand-mark"></span>
        <span class="brand-name">Brightcoil Power Electrical</span>
      </div>
      <address class="company-details">
        <div class="company-title">Brightcoil Power Electrical</div>
        <div>8/22-24 Larkin Rd, Tolvern 2087</div>
        <div><span class="label">Lic. No:</span> 48162</div>
        <div><span class="label">ABN:</span> 42 597 214 630</div>
        <div class="detail-row">(02) 9471 3825 <span class="detail-icon"></span></div>
        <div class="detail-row">0427 593 168 <span class="detail-icon"></span></div>
        <div class="detail-row">brightcoilpower.com.au <span class="detail-icon"></span></div>
        <div class="detail-row">info@brightcoilpower.com.au</div>
      </address>
    </header>

    <section class="letter">
      <div class="salutation">Dear Mr. Harlow,</div>
      <p>Lorem Ipsum is simply dummy text of the printing and typesetting industry. Lorem Ipsum has been the industry's standard dummy text ever since the 1500s, when an unknown printer took a galley of type and scrambled it to make a type specimen book. It has survived not only five centuries, but also the leap into electronic typesetting, remaining essentially unchanged.</p>
      <p>The standard chunk of Lorem Ipsum used since the 1500s is reproduced below for those interested. Sections 1.10.32 and 1.10.33 from "de Finibus Bonorum et Malorum" by Varro are also reproduced in their exact original form, accompanied by English versions from the 1914 translation by H. Ellery.</p>
      <p>Lorem Ipsum is simply dummy text of the printing and typesetting industry. Lorem Ipsum has been the industry's standard dummy text ever since the 1500s, when an unknown printer took a galley of type and scrambled it to make a type specimen book. It has survived not only five centuries, but also the leap into electronic typesetting, remaining essentially unchanged. It was popularised in the</p>
      <div class="sign-off">Sincerely Your,</div>
      <div class="signature">your name</div>
      <div class="signer">Name Last Name<br>Company Name</div>
    </section>

    <svg class="footer-wave" viewBox="0 0 523 740" aria-hidden="true">
      <path fill="var(--brand-orange)" d="M150,740 C260,720 330,660 380,590 C420,535 470,520 523,512 L523,528 C475,536 432,556 398,606 C350,676 280,722 150,740 Z"/>
      <path fill="var(--brand-dark)" d="M0,740 C230,738 320,690 392,612 C430,566 474,544 523,536 L523,740 Z"/>
    </svg>
    <div class="footer-web">www.brightcoilpower.com.au</div>
  </main>
</body>
</html>
```